Regroupons Nos Caissettes

RegrouponsNosCaissettes is crowdshipping marketplace that allows his members to get together to organize a container from country A to country B. Thereby they are able to import small volumes of products at low prices.

How it works: https://poolyourcrate.example.co.uk/Containers/

One example of website that we could use for reference: https://poolyourcrate.example.co.uk/

Target Market(s)

Crowdshipping - Freight forwarder -

Coding

Coded - Design and coding required

Number of Pages Required

3 page

Font styles to use
Sans Serif

Colors
f04a50
886aae
34a6d7
fbee3e
33b8a4

Requirements
Must have
• Landing page: https://poolyourcrate.example.co.uk/Containers/

Enquire: https://poolyourcrate.example.co.uk/Enquire/?subject=Space%20on%20container%20to%20Australia%20-%20Adelaide%20(22.08.2020)

```html
<!DOCTYPE html>
<html lang="en">
<head>
<meta charset="utf-8">
<title>Regroupons Nos Caissettes</title>
<link href="https://fonts.googleapis.com/css2?family=Lato:wght@400;700;900&display=swap" rel="stylesheet">
<style>
:root{
  --red:#f04a50;
  --red-deep:#e5323b;
  --purple:#886aae;
  --blue:#34a6d7;
  --blue-title:#2e92cc;
  --yellow:#fbee3e;
  --teal:#33b8a4;
  --teal-nav:#2fae93;
  --ink:#1f1f1f;
  --text:#2b2b2b;
  --grey-band:#ececec;
  --line:#dcdcdc;
  --footer:#1a1a1a;
  --navy:#14234a;
}
*{box-sizing:border-box;margin:0;padding:0}
html,body{width:722px;height:1200px;overflow:hidden}
body{font-family:'Lato',sans-serif;color:var(--text);
  background:linear-gradient(180deg,#dcecf8 0,#eef5fb 120px,#fff 300px);position:relative}
.abs{position:absolute}

/* header */
.brand{left:45px;top:18px;display:flex;align-items:center;gap:8px}
.brand-mark{width:42px;height:42px;border-radius:50%;background:var(--navy)}
.brand-name{font-weight:900;font-size:12.5px;line-height:13px;color:var(--navy);text-transform:uppercase;width:110px}
.brand-tag{font-size:6.5px;color:#9c7a1e;margin-top:2px;text-transform:none;font-weight:400}
.phone{right:44px;top:9px;display:flex;align-items:center;gap:10px;color:var(--red-deep);font-weight:700;font-size:13.5px}
.phone-dot{width:23px;height:23px;border-radius:50%;background:var(--red-deep);display:flex;align-items:center;justify-content:center}
.main-nav{left:261px;top:41px;width:417px;height:27px;background:var(--teal-nav);display:flex}
.main-nav a{color:#fff;text-decoration:none;font-size:8.5px;font-weight:700;display:flex;align-items:center;padding:0 12px;text-transform:uppercase}
.main-nav a.active{background:var(--blue);padding:0 15px}

/* hero */
.hero{left:45px;top:76px;width:633px;height:211px;background:#e9e9e9;overflow:hidden}
.hero-photo{position:absolute;left:230px;top:0;width:403px;height:211px;
  background:linear-gradient(90deg,#e9e9e9 0,#c8b29b 30%,#8b6a55 55%,#a85a4b 75%,#4f5f78 100%)}
.hero h1{position:absolute;left:17px;top:44px;font-size:19.5px;line-height:24px;font-weight:900;color:var(--ink);width:330px}
.search{position:absolute;left:18px;top:98px;width:298px;height:31px;background:#fff;border:1px solid #bbb;font-size:8.5px;padding:0 9px;display:flex;align-items:center;color:#333}
.btn-post{position:absolute;left:18px;top:134px;width:96px;height:31px;background:var(--red-deep);color:#fff;font-weight:700;font-size:12.5px;display:flex;align-items:center;justify-content:center}

/* welcome */
.welcome{left:90px;top:307px;width:542px;text-align:center}
.welcome h2{color:var(--blue-title);font-size:19.5px;font-weight:700}
.welcome p{font-size:8.5px;line-height:16.7px;margin-top:7px;color:#222}
.divider{left:45px;top:417px;width:633px;height:1px;background:var(--line)}

/* section heads */
.sec-head{height:30px;background:var(--grey-band);border-left:6px solid var(--red-deep);color:var(--blue-title);font-weight:700;font-size:14px;display:flex;align-items:center;padding-left:9px}

/* deal cards */
.deal{left:45px;width:361px;height:134px;border:1px solid var(--purple);border-bottom:3px solid var(--purple);background:#fff}
.deal-ribbon{position:absolute;left:-10px;top:10px;width:334px;height:26px;background:var(--teal);color:#fff;font-size:11.5px;display:flex;align-items:center;padding-left:50px}
.deal-fold{position:absolute;left:-10px;top:36px;width:0;height:0;border-top:7px solid #222;border-left:10px solid transparent}
.flag{position:absolute;left:4px;top:1px;width:24px;height:24px;border-radius:50%;border:2px solid #fff}
.crate{position:absolute;left:8px;top:48px;width:58px;height:33px;background:linear-gradient(180deg,#d8333a,#a91f26)}
.space{position:absolute;left:78px;top:52px;font-size:13px;color:var(--ink)}
.space sup{font-size:7px}
.deal-btns{position:absolute;left:77px;top:77px;display:flex;gap:4px}
.deal-btns span{height:18px;font-size:8px;display:flex;align-items:center;padding:0 8px}
.btn-view{background:var(--red-deep);color:#fff}
.btn-enq{background:var(--yellow);color:#222;font-weight:700;padding:0 10px!important}
.deal-meta{position:absolute;left:0;top:104px;width:100%;border-top:1px solid var(--line);font-size:8.5px;padding:7px 9px;color:#222}

/* how it works */
.step{left:424px;width:254px;display:flex;gap:14px}
.step-icon{flex:none;width:53px;height:53px;border-radius:50%;border:1px solid #888;display:flex;align-items:center;justify-content:center}
.step-icon i{width:26px;height:26px;border-radius:50%;display:block}
.step p{font-size:8.5px;line-height:15px;color:#222;padding-top:4px}

.announce{left:424px;top:757px;width:254px;font-size:8.5px;line-height:15px;color:#222}
.btn-more{left:424px;top:821px;width:91px;height:28px;background:var(--blue);color:#fff;font-size:10.5px;display:flex;align-items:center;justify-content:center}

/* footer */
.site-footer{left:0;top:1086px;width:722px;height:114px;background:var(--footer);color:#fff;text-align:center}
.foot-nav{display:flex;justify-content:center;gap:24px;margin-top:26px;font-size:8.5px;font-weight:700;text-transform:uppercase}
.copy{font-size:7.5px;margin-top:14px}
.social{display:flex;justify-content:center;gap:14px;margin-top:12px}
.social i{width:14px;height:14px;border-radius:50%;background:#555;display:block}
</style>
</head>
<body>

<header>
  <div class="brand abs">
    <span class="brand-mark"></span>
    <div class="brand-name">Regroupons Nos Caissettes<div class="brand-tag">Groupage maritime entre particuliers</div></div>
  </div>
  <div class="phone abs">
    <span class="phone-dot"><svg width="11" height="11" viewBox="0 0 24 24"><path fill="#fff" d="M6.6 10.8a15 15 0 0 0 6.6 6.6l2.2-2.2c.3-.3.7-.4 1-.2 1.1.4 2.3.6 3.6.6.6 0 1 .4 1 1V20c0 .6-.4 1-1 1A17 17 0 0 1 3 4c0-.6.4-1 1-1h3.5c.6 0 1 .4 1 1 0 1.2.2 2.4.6 3.6.1.3 0 .7-.2 1z"/></svg></span>
    1-800-555-0142
  </div>
  <nav class="main-nav abs">
    <a class="active">Home</a><a>Advertisement</a><a>How it works</a><a>FAQ</a><a>Registration</a><a>Login</a>
  </nav>
</header>

<section class="hero abs">
  <div class="hero-photo" role="img" aria-label="Photo of a smiling couple looking at a laptop among moving boxes"></div>
  <h1>Find or rent space in a container has never been so easy</h1>
  <div class="search">Search ad keyword</div>
  <div class="btn-post">Post an Ad</div>
</section>

<section class="welcome abs">
  <h2>Welcome to Our Website</h2>
  <p>Nulla tincidunt dapibus urna, ut viverra quam mollis a. Suspendisse lobortis, magna eget dapibus maximus, enim tortor accumsan risus, eget euismod massa quam et magna. Nullam tristique sit amet eros eget aliquet. Mauris scelerisque aliquet velit eget ultrices. In lacinia dictum sem, eu pretium ex sollicitudin et.</p>
</section>
<div class="divider abs"></div>

<div class="sec-head abs" style="left:45px;top:435px;width:361px">Last Minute Container Deals</div>
<div class="sec-head abs" style="left:424px;top:435px;width:254px">How it Works</div>

<article class="deal abs" style="top:481px">
  <div class="deal-ribbon"><span class="flag" style="background:#1f3a8a"></span>Australia - Adelaide</div><span class="deal-fold"></span>
  <div class="crate" role="img" aria-label="Red shipping container"></div>
  <div class="space">Space Left: 60 ft<sup>3</sup></div>
  <div class="deal-btns"><span class="btn-view">View More</span><span class="btn-enq">Enquire About Space</span></div>
  <div class="deal-meta">Loading Date: 22.08.2020 &nbsp;/&nbsp; Transit Time: 4 to 6 weeks</div>
</article>
<article class="deal abs" style="top:627px">
  <div class="deal-ribbon"><span class="flag" style="background:#d52b1e"></span>Canada - Toronto</div><span class="deal-fold"></span>
  <div class="crate" role="img" aria-label="Red shipping container"></div>
  <div class="space">Space Left: 60 ft<sup>3</sup></div>
  <div class="deal-btns"><span class="btn-view">View More</span><span class="btn-enq">Enquire About Space</span></div>
  <div class="deal-meta">Loading Date: 22.08.2020 &nbsp;/&nbsp; Transit Time: 4 to 6 weeks</div>
</article>
<article class="deal abs" style="top:773px">
  <div class="deal-ribbon"><span class="flag" style="background:#c8102e"></span>USA - Miami</div><span class="deal-fold"></span>
  <div class="crate" role="img" aria-label="Red shipping container"></div>
  <div class="space">Space Left: 60 ft<sup>3</sup></div>
  <div class="deal-btns"><span class="btn-view">View More</span><span class="btn-enq">Enquire About Space</span></div>
  <div class="deal-meta">Loading Date: 22.08.2020 &nbsp;/&nbsp; Transit Time: 4 to 6 weeks</div>
</article>
<article class="deal abs" style="top:921px">
  <div class="deal-ribbon"><span class="flag" style="background:#007a4d"></span>South Africa - Cape Town</div><span class="deal-fold"></span>
  <div class="crate" role="img" aria-label="Red shipping container"></div>
  <div class="space">Space Left: 60 ft<sup>3</sup></div>
  <div class="deal-btns"><span class="btn-view">View More</span><span class="btn-enq">Enquire About Space</span></div>
  <div class="deal-meta">Loading Date: 22.08.2020 &nbsp;/&nbsp; Transit Time: 4 to 6 weeks</div>
</article>

<div class="step abs" style="top:480px">
  <div class="step-icon" role="img" aria-label="Support agent illustration"><i style="background:#f08a4b"></i></div>
  <p>Inscrivez-vous et publiez votre annonce de location, de recherche d'espace libre ou de mutualisation dans un conteneur.</p>
</div>
<div class="step abs" style="top:559px">
  <div class="step-icon" role="img" aria-label="Phone contact illustration"><i style="background:#5aa9e6"></i></div>
  <p>Prenez directement contact avec l'auteur de l'annonce.</p>
</div>
<div class="step abs" style="top:638px">
  <div class="step-icon" role="img" aria-label="Money bag illustration"><i style="background:#e8393f"></i></div>
  <p>Le tour est joué, vous avez fait des économies en partageant votre conteneur.</p>
</div>

<div class="sec-head abs" style="left:424px;top:716px;width:254px">Latest Announcements</div>
<p class="announce abs">Aliquam est sem, cursus eu suscipit id, aliquam ac ante. Vestibulum massa est, rutrum ut tellus a, iaculis ullamcorper augue sed elit nec lacus fringilla.</p>
<div class="btn-more abs">More Listings</div>

<footer class="site-footer abs">
  <nav class="foot-nav"><span>Home</span><span>Advertisement</span><span>How it works</span><span>FAQ</span><span>Registration</span><span>Login</span></nav>
  <p class="copy">Copyright© 2020 Company Name All Right Reserved</p>
  <div class="social"><i></i><i></i><i></i><i></i><i></i></div>
</footer>

</body>
</html>
```